Major Chiropractic Campaign Shown to 7 million people in print and online

Please design a SIMPLE and CLEAR advert in various sizes that will be used for print and media.

1/ Newspaper Print size: 381 x 272 with border and MUST be able to stand out in a newspaper

2/ Media: 5 sizes - rotating .gif 2 frames
- 160x600
- 728x90
- 300x250
- 300x600
- 320x50

3/ Facebook (must pass: http://ninetenthsgauge.info)
- 300x315

Target Market(s)

females
35 - 54 yo
educated

Industry/Entity Type

Media

Font styles to use
Sans Serif

Colors
3176b5
33a6d7
ffffff
ec1f27
1b1b1b
919191
9bcb3c

Requirements
Must have
• clean
• easy to read
• strong CALL TO ACTION
• professional
• well designed book cover with the title " The Quiet Pathway Linking Your Nerves and Posture Revealed"
• The book MUST look like it's a professional report
• the winning design WILL show all design on a single page

```html
<!DOCTYPE html>
<html lang="en">
<head>
<meta charset="utf-8">
<title>Free Report Campaign – Ad Sizes</title>
<link href="https://fonts.googleapis.com/css2?family=Oswald:wght@400&family=Raleway:wght@400;500;700;800&family=Roboto:wght@400;500;700;900&display=swap" rel="stylesheet">
<style>
:root{
  --board:#a3a4a6;
  --ink:#1b1b1b;
  --navy:#27318a;
  --navy-deep:#1c2462;
  --red:#ec1f27;
  --green:#9bcb3c;
  --green-dark:#6fa41d;
  --sky:#33a6d7;
  --blue:#3176b5;
  --paper:#ffffff;
  --mist:#d3d6dc;
  --art-light:#2f55b4;
  --art-deep:#0b1548;
}
*{box-sizing:border-box;margin:0;padding:0}
html,body{width:1200px;height:1000px;overflow:hidden}
body{background:var(--board);font-family:"Roboto",Arial,sans-serif;color:var(--ink)}
.board{position:relative;width:1200px;height:1000px}

/* size labels */
.size-label{position:absolute;font-family:"Oswald","Arial Narrow",sans-serif;font-size:15px;color:var(--ink);letter-spacing:.02em}

/* ad frame */
.ad{position:absolute;overflow:hidden;background:linear-gradient(180deg,var(--paper) 35%,var(--mist) 100%)}
.ad__corner{position:absolute;left:0;top:0;background:var(--red);clip-path:polygon(0 0,100% 0,0 100%)}
.ad__corner-text{position:absolute;color:var(--paper);font-weight:700;letter-spacing:-.04em;line-height:.85;text-align:center}
.ad__ground{position:absolute;left:0;bottom:0;width:100%}
.ad__ground polygon{fill:var(--navy-deep)}
.headline{position:absolute;font-weight:400;line-height:1.3;color:var(--ink)}
.headline strong{font-weight:900}
.cta{position:absolute;display:flex;align-items:center;justify-content:center;border-radius:6px;
  background:linear-gradient(180deg,#c8ec7a 0%,var(--green) 45%,var(--green-dark) 100%);
  border:1px solid var(--green-dark);box-shadow:0 2px 3px rgba(0,0,0,.3);
  font-family:"Roboto",Arial,sans-serif;font-weight:700;color:#15320a;white-space:nowrap}

/* book: light report */
.book{position:absolute;width:10em;height:15.5em;box-shadow:.3em .4em .6em rgba(0,0,0,.35)}
.book__cover{position:absolute;left:0;top:0;width:9.4em;height:100%;background:var(--paper);overflow:hidden}
.book__spine{position:absolute;right:0;top:0;width:.6em;height:100%;background:linear-gradient(90deg,#3b47a8,var(--navy-deep))}
.cover__top{border-top:.45em solid var(--navy);padding:.35em .6em .3em;font-family:"Raleway",sans-serif;font-size:.85em;color:var(--navy);font-weight:400;line-height:1}
.cover__top b{font-weight:800}
.cover__art{height:5.9em;background:linear-gradient(160deg,var(--art-light) 0%,#1a2f80 50%,var(--art-deep) 100%)}
.cover__title{padding:.55em .6em 0;font-family:"Raleway",sans-serif;color:var(--navy);line-height:1}
.cover__title .t1{display:block;font-size:1.25em;font-weight:500}
.cover__title .t2{display:block;font-size:1.4em;font-weight:800;letter-spacing:-.01em}
.cover__sub{margin:.3em .6em 0;padding-top:.2em;border-top:.06em solid var(--navy);font-family:"Raleway",sans-serif;font-size:.38em;font-weight:700;color:var(--navy);letter-spacing:.02em}
.cover__blurb{margin:.5em .6em 0;padding-top:.3em;border-top:.04em solid var(--navy);font-size:.36em;color:#444;line-height:1.3}

/* book: dark report */
.book--dark .book__cover{background:linear-gradient(180deg,#26357a,#141c4e)}
.dark__art{height:7.4em;background:linear-gradient(180deg,rgba(70,130,220,.45) 0%,rgba(40,70,160,.2) 70%,transparent 100%)}
.dark__flag{position:absolute;right:.6em;top:.5em;font-size:.55em;font-weight:700;color:var(--paper);line-height:1;text-align:right}
.dark__title{padding:0 .45em;font-weight:900;font-size:1.02em;color:var(--paper);line-height:.98;letter-spacing:-.04em}
.dark__title em{font-style:normal;color:#5fbcf0}
.dark__blurb{margin:.5em .7em 0;font-size:.34em;color:#d6dcf0;line-height:1.3}

/* placements */
.ad--leader{left:18px;top:35px;width:730px;height:90px}
.ad--leader .ad__corner{width:135px;height:150px}
.ad--leader .ad__corner-text{left:10px;top:12px;font-size:21px}
.ad--leader .headline{left:107px;top:20px;font-size:23px;line-height:1.25}
.ad--leader .headline strong{font-size:27px}
.ad--leader .cta{left:400px;top:52px;width:93px;height:24px;font-size:9px}
.ad--leader .book--dark{left:569px;top:3px;font-size:5.2px}
.ad--leader .book--light{left:630px;top:3px;font-size:5.2px}

.ad--rect-a{left:880px;top:28px;width:300px;height:250px}
.ad--rect-b{left:880px;top:313px;width:300px;height:250px}
.ad--rect-a .ad__corner,.ad--rect-b .ad__corner{width:125px;height:135px}
.ad--rect-a .ad__corner-text,.ad--rect-b .ad__corner-text{left:10px;top:12px;font-size:19px}
.ad--rect-a .headline,.ad--rect-b .headline{left:8px;top:87px;width:126px;font-size:14px;text-align:right}
.ad--rect-a .headline strong,.ad--rect-b .headline strong{font-size:21px}
.ad--rect-a .cta,.ad--rect-b .cta{left:40px;top:178px;width:90px;height:24px;font-size:9px}
.ad--rect-a .book{left:145px;top:12px;font-size:12.7px}
.ad--rect-b .book{left:145px;top:16px;font-size:12.5px}

.ad--sky{left:22px;top:177px;width:161px;height:600px}
.ad--sky .ad__corner{width:125px;height:110px}
.ad--sky .ad__corner-text{left:6px;top:12px;font-size:18px}
.ad--sky .book{left:8px;top:92px;font-size:13.8px}
.ad--sky .headline{left:0;top:328px;width:146px;font-size:16px;text-align:right}
.ad--sky .headline strong{font-size:24px}
.ad--sky .cta{left:23px;top:440px;width:117px;height:31px;font-size:11px}

.ad--half{left:200px;top:177px;width:301px;height:601px}
.ad--half .ad__corner{width:165px;height:150px}
.ad--half .ad__corner-text{left:10px;top:14px;font-size:24px}
.ad--half .book{left:44px;top:68px;font-size:22px}
.ad--half .headline{left:0;top:428px;width:301px;font-size:19px;text-align:center;line-height:1.45}
.ad--half .headline strong{font-size:22px}
.ad--half .cta{left:80px;top:496px;width:138px;height:37px;font-size:13px}

.ad--social{left:527px;top:181px;width:300px;height:315px}
.ad--social .ad__corner{width:110px;height:105px}
.ad--social .ad__corner-text{left:6px;top:10px;font-size:16px}
.ad--social .book{left:125px;top:14px;font-size:15.5px}
.ad--social .headline{left:0;top:128px;width:117px;font-size:14px;text-align:right}
.ad--social .headline strong{font-size:21px}
.ad--social .cta{left:7px;top:217px;width:110px;height:29px;font-size:11px;font-weight:500}

.ad--print{left:524px;top:571px;width:590px;height:420px}
.ad--print .ad__corner{width:160px;height:125px}
.ad--print .ad__corner-text{left:10px;top:12px;font-size:22px}
.print__title{position:absolute;left:30px;top:92px;font-family:"Raleway",sans-serif;color:var(--navy);line-height:1}
.print__title .t1{display:block;font-size:40px;font-weight:400;letter-spacing:.01em}
.print__title .t2{display:block;font-size:40px;font-weight:800;margin-top:4px}
.print__sub{position:absolute;left:30px;top:176px;width:302px;padding-top:6px;border-top:1.5px solid var(--navy);font-family:"Raleway",sans-serif;font-size:11px;font-weight:700;color:var(--navy);letter-spacing:.03em}
.ad--print .headline{left:28px;top:212px;font-size:23px;line-height:1.42}
.ad--print .headline strong{font-size:28px}
.ad--print .cta{left:29px;top:320px;width:150px;height:40px;font-size:15px}
.ad--print .book{left:342px;top:38px;font-size:21.5px}
.print__url{position:absolute;left:30px;bottom:12px;font-size:18px;color:var(--paper);letter-spacing:.01em}

.ad--mobile{left:57px;top:828px;width:320px;height:55px}
.ad--mobile .ad__corner{width:62px;height:95px}
.ad--mobile .ad__corner-text{left:4px;top:8px;font-size:10px}
.ad--mobile .headline{left:56px;top:13px;font-size:10.5px;line-height:1.3}
.ad--mobile .headline strong{font-size:12px}
.ad--mobile .cta{left:188px;top:31px;width:46px;height:13px;font-size:5px;border-radius:3px}
.ad--mobile .book{left:236px;top:1px;font-size:8.4px}
</style>
</head>
<body>
<main class="board">

  <!-- 728 x 90 leaderboard -->
  <span class="size-label" style="left:18px;top:10px">728X90</span>
  <section class="ad ad--leader" aria-label="728 by 90 leaderboard">
    <div class="ad__corner"></div>
    <div class="ad__corner-text">Free<br>Report</div>
    <p class="headline">Doctors Explain the Quiet Pathway<br>that Controls your <strong>Health</strong></p>
    <span class="cta">GET FREE REPORT</span>
    <div class="book book--dark">
      <div class="book__cover">
        <div class="dark__art" role="img" aria-label="Brain and head outline illustration"></div>
        <div class="dark__flag">Free<br>Report</div>
        <p class="dark__title">The<em>Quiet</em> Pathway Linking Your <em>Nerves&amp;Posture</em> Revealed</p>
      </div>
      <div class="book__spine"></div>
    </div>
    <div class="book book--light">
      <div class="book__cover">
        <div class="cover__top">FREE <b>REPORT</b></div>
        <div class="cover__art" role="img" aria-label="Glowing neuron network illustration"></div>
        <div class="cover__title"><span class="t1">THE QUIET</span><span class="t2">PATHWAY</span></div>
        <div class="cover__sub">LINKING YOUR NERVES AND POSTURE REVEALED</div>
        <p class="cover__blurb">Chiropractors explain the quiet pathway that controls your body &amp; keeps you healthy.</p>
      </div>
      <div class="book__spine"></div>
    </div>
  </section>

  <!-- 300 x 250 (dark cover) -->
  <span class="size-label" style="left:880px;top:6px">300X250</span>
  <section class="ad ad--rect-a" aria-label="300 by 250 rectangle">
    <div class="ad__corner"></div>
    <div class="ad__corner-text">Free<br>Report</div>
    <svg class="ad__ground" viewBox="0 0 300 40" height="40" preserveAspectRatio="none" aria-hidden="true"><polygon points="0,18 40,12 90,22 300,36 300,40 0,40"/></svg>
    <p class="headline">Doctors Explain<br>the Quiet Pathway<br>that Controls your<br><strong>Health</strong></p>
    <span class="cta">GET FREE REPORT</span>
    <div class="book book--dark">
      <div class="book__cover">
        <div class="dark__art" role="img" aria-label="Brain and head outline illustration"></div>
        <div class="dark__flag">Free<br>Report</div>
        <p class="dark__title">The<em>Quiet</em> Pathway Linking Your <em>Nerves&amp;Posture</em> Revealed</p>
        <p class="dark__blurb">Chiropractors explain the quiet pathway that controls your body &amp; keeps you healthy.</p>
      </div>
      <div class="book__spine"></div>
    </div>
  </section>

  <!-- 300 x 250 (light cover) -->
  <span class="size-label" style="left:880px;top:291px">300X250</span>
  <section class="ad ad--rect-b" aria-label="300 by 250 rectangle">
    <div class="ad__corner"></div>
    <div class="ad__corner-text">Free<br>Report</div>
    <svg class="ad__ground" viewBox="0 0 300 40" height="40" preserveAspectRatio="none" aria-hidden="true"><polygon points="0,14 45,8 95,20 300,34 300,40 0,40"/></svg>
    <p class="headline">Doctors Explain<br>the Quiet Pathway<br>that Controls your<br><strong>Health</strong></p>
    <span class="cta">GET FREE REPORT</span>
    <div class="book book--light">
      <div class="book__cover">
        <div class="cover__top">FREE <b>REPORT</b></div>
        <div class="cover__art" role="img" aria-label="Glowing neuron network illustration"></div>
        <div class="cover__title"><span class="t1">THE QUIET</span><span class="t2">PATHWAY</span></div>
        <div class="cover__sub">LINKING YOUR NERVES AND POSTURE REVEALED</div>
        <p class="cover__blurb">Chiropractors explain the quiet pathway that controls your body &amp; keeps you healthy.</p>
      </div>
      <div class="book__spine"></div>
    </div>
  </section>

  <!-- 160 x 600 skyscraper -->
  <span class="size-label" style="left:22px;top:156px">160X600</span>
  <section class="ad ad--sky" aria-label="160 by 600 skyscraper">
    <div class="ad__corner"></div>
    <div class="ad__corner-text">Free<br>Report</div>
    <svg class="ad__ground" viewBox="0 0 161 95" height="95" preserveAspectRatio="none" aria-hidden="true"><polygon points="0,12 30,0 75,10 161,24 161,95 0,95"/></svg>
    <div class="book book--dark">
      <div class="book__cover">
        <div class="dark__art" role="img" aria-label="Brain and head outline illustration"></div>
        <div class="dark__flag">Free<br>Report</div>
        <p class="dark__title">The<em>Quiet</em> Pathway Linking Your <em>Nerves&amp;Posture</em> Revealed</p>
        <p class="dark__blurb">Chiropractors explain the quiet pathway that controls your body &amp; keeps you healthy.</p>
      </div>
      <div class="book__spine"></div>
    </div>
    <p class="headline">Doctors Explain<br>the Quiet Pathway<br>that Controls your<br><strong>Health</strong></p>
    <span class="cta">GET FREE REPORT</span>
  </section>

  <!-- 300 x 600 half page -->
  <span class="size-label" style="left:202px;top:156px">300X600</span>
  <section class="ad ad--half" aria-label="300 by 600 half page">
    <div class="ad__corner"></div>
    <div class="ad__corner-text">Free<br>Report</div>
    <svg class="ad__ground" viewBox="0 0 301 66" height="66" preserveAspectRatio="none" aria-hidden="true"><polygon points="0,10 60,0 130,8 301,20 301,66 0,66"/></svg>
    <div class="book book--light">
      <div class="book__cover">
        <div class="cover__top">FREE <b>REPORT</b></div>
        <div class="cover__art" role="img" aria-label="Glowing neuron network illustration"></div>
        <div class="cover__title"><span class="t1">THE QUIET</span><span class="t2">PATHWAY</span></div>
        <div class="cover__sub">LINKING YOUR NERVES AND POSTURE REVEALED</div>
        <p class="cover__blurb">Chiropractors explain the quiet pathway that controls your body &amp; keeps you healthy.</p>
      </div>
      <div class="book__spine"></div>
    </div>
    <p class="headline">Doctors Explain the Quiet Pathway<br>that Controls your <strong>Health</strong></p>
    <span class="cta">GET FREE REPORT</span>
  </section>

  <!-- Facebook 300 x 315 -->
  <span class="size-label" style="left:528px;top:158px">FACEBOOK AD 300X315 @20% TEXT</span>
  <section class="ad ad--social" aria-label="300 by 315 social ad">
    <div class="ad__corner"></div>
    <div class="ad__corner-text">Free<br>Report</div>
    <svg class="ad__ground" viewBox="0 0 300 45" height="45" preserveAspectRatio="none" aria-hidden="true"><polygon points="0,8 30,0 80,10 300,22 300,45 0,45"/></svg>
    <div class="book book--light">
      <div class="book__cover">
        <div class="cover__top">FREE <b>REPORT</b></div>
        <div class="cover__art" role="img" aria-label="Glowing neuron network illustration"></div>
        <div class="cover__title"><span class="t1">THE QUIET</span><span class="t2">PATHWAY</span></div>
        <div class="cover__sub">LINKING YOUR NERVES AND POSTURE REVEALED</div>
        <p class="cover__blurb">Chiropractors explain the quiet pathway that controls your body &amp; keeps you healthy.</p>
      </div>
      <div class="book__spine"></div>
    </div>
    <p class="headline">Doctors Explain<br>the Quiet Pathway<br>that Controls your<br><strong>Health</strong></p>
    <span class="cta">GET FREE REPORT</span>
  </section>

  <!-- Newspaper 381 x 272 -->
  <span class="size-label" style="left:524px;top:540px;font-size:19px">NEWS PAPER AD&nbsp; 381 X 272</span>
  <section class="ad ad--print" aria-label="Newspaper advertisement">
    <div class="ad__corner"></div>
    <div class="ad__corner-text">Free<br>Report</div>
    <svg class="ad__ground" viewBox="0 0 590 70" height="70" preserveAspectRatio="none" aria-hidden="true"><polygon points="0,12 50,4 150,10 590,16 590,70 0,70"/></svg>
    <div class="print__title"><span class="t1">THE QUIET</span><span class="t2">PATHWAY</span></div>
    <div class="print__sub">LINKING YOUR NERVES AND POSTURE REVEALED</div>
    <p class="headline">Doctors Explain the Quiet<br>Pathway that Controls<br>your <strong>Health</strong></p>
    <span class="cta">GET FREE REPORT</span>
    <div class="book book--light">
      <div class="book__cover">
        <div class="cover__top">FREE <b>REPORT</b></div>
        <div class="cover__art" role="img" aria-label="Glowing neuron network illustration"></div>
        <div class="cover__title"><span class="t1">THE QUIET</span><span class="t2">PATHWAY</span></div>
        <div class="cover__sub">LINKING YOUR NERVES AND POSTURE REVEALED</div>
        <p class="cover__blurb">Chiropractors explain the quiet pathway that controls your body &amp; keeps you healthy.</p>
      </div>
      <div class="book__spine"></div>
    </div>
    <p class="print__url">www.spinalinsight.com.au |</p>
  </section>

  <!-- 320 x 50 mobile -->
  <span class="size-label" style="left:330px;top:808px">320X50</span>
  <section class="ad ad--mobile" aria-label="320 by 50 mobile banner">
    <div class="ad__corner"></div>
    <div class="ad__corner-text">Free<br>Report</div>
    <p class="headline">Doctors Explain the Quiet Pathway<br>that Controls your <strong>Health</strong></p>
    <span class="cta">GET FREE REPORT</span>
    <div class="book book--dark">
      <div class="book__cover">
        <div class="dark__art" role="img" aria-label="Brain and head outline illustration" style="height:2.2em"></div>
        <p class="dark__title">The<em>Quiet</em> Pathway Linking Your <em>Nerves&amp;Posture</em> Revealed</p>
      </div>
      <div class="book__spine"></div>
    </div>
  </section>

</main>
</body>
</html>
```